Oru Pest Control Booth Backdrop

Looking for a family owned and operated Pest control with safest products for family and pets. Attaching our old design and looking for a new and improved idea. Backdrop is 7.5'x7.5'

```html
<!DOCTYPE html>
<html lang="en">
<head>
<meta charset="utf-8">
<title>Oru Pest Control Booth Backdrop</title>
<link href="https://fonts.googleapis.com/css2?family=Anton&family=Archivo:ital,wght@0,600;0,800;1,900&family=Outfit:wght@400;500&display=swap" rel="stylesheet">
<style>
  :root {
    --stage: #8bb8f5;
    --paper: #ffffff;
    --brand-red: #d9462b;
    --ink: #141414;
    --photo-wall: #b9b3a8;
    --photo-lawn: #9fb27a;
    --photo-sky: #c9d6df;
    --bug: #d6d6d6;
  }
  * { margin: 0; padding: 0; box-sizing: border-box; }
  html, body { width: 1200px; height: 598px; overflow: hidden; background: var(--stage); }
  .stage { position: relative; width: 1200px; height: 598px; }
  .backdrop {
    position: absolute; left: 288px; top: 22px;
    width: 1075px; height: 953px;
    background: var(--paper);
    transform: scale(0.58); transform-origin: 0 0;
    font-family: "Outfit", sans-serif; color: var(--ink);
  }
  .abs { position: absolute; }
  .brand { left: 78px; top: 92px; display: flex; align-items: center; gap: 16px; }
  .brand-mark { width: 40px; height: 40px; background: var(--brand-red); }
  .brand-name { font-family: "Archivo", sans-serif; font-weight: 800; font-size: 52px; color: var(--ink); white-space: nowrap; }
  .safer-tag {
    left: 48px; top: 238px; width: 285px; height: 115px;
    background: var(--ink); border-radius: 8px; transform: rotate(-2deg);
    color: #fff; font-family: "Archivo", sans-serif; font-weight: 600; font-size: 76px;
    display: flex; align-items: center; justify-content: center;
  }
  .headline-organic {
    left: 56px; top: 338px; width: 640px; white-space: nowrap;
    font-family: "Anton", sans-serif; font-size: 172px; line-height: 1;
    color: var(--brand-red); transform-origin: 0 0;
    transform: skewX(-8deg) scaleX(0.62);
  }
  .headline-products {
    left: 58px; top: 500px; font-family: "Archivo", sans-serif; white-space: nowrap;
    font-style: italic; font-weight: 900; font-size: 86px; line-height: 1; letter-spacing: -2px;
    transform: scaleX(0.82); transform-origin: 0 0;
  }
  .friendly-band {
    left: 62px; top: 610px; width: 552px; height: 102px;
    background: var(--brand-red); border-radius: 4px; color: #fff; white-space: nowrap;
    font-size: 48px; font-weight: 500; display: flex; align-items: center; padding-left: 38px;
  }
  .service-box {
    top: 747px; width: 191px; height: 158px; border: 1.5px solid var(--brand-red); border-radius: 4px;
    display: flex; flex-direction: column; justify-content: center; align-items: center; gap: 10px;
    font-size: 22px; line-height: 1.1; text-align: center;
  }
  .service-box li { list-style: none; }
  .service-box .accent { color: var(--brand-red); }
  .tick { display: inline-block; width: 16px; height: 12px; margin-right: 4px; }
  .photo { left: 740px; width: 290px; border-radius: 4px; }
  .photo-spraying { top: 47px; height: 465px; background: linear-gradient(160deg, var(--photo-wall), #8a7b6b 60%, #e07a3a); }
  .photo-sprayer { top: 532px; height: 176px; background: linear-gradient(90deg, var(--photo-lawn), #c8c4bc); }
  .photo-inspecting { top: 728px; height: 177px; background: linear-gradient(120deg, var(--photo-sky), #e59a60); }
  .bug { background: var(--bug); border-radius: 50%; }
</style>
</head>
<body>
<div class="stage">
  <div class="backdrop">
    <div class="abs brand"><span class="brand-mark"></span><span class="brand-name">Oru Pest Control</span></div>

    <div class="abs bug" style="left:492px;top:228px;width:62px;height:62px" role="img" aria-label="Fly illustration"></div>

    <div class="abs safer-tag">SAFER</div>
    <div class="abs headline-organic">ORGANIC BASED</div>
    <div class="abs headline-products">PRODUCTS</div>

    <div class="abs friendly-band">Family &amp; Pet Friendly.</div>
    <div class="abs bug" style="left:540px;top:530px;width:66px;height:84px" role="img" aria-label="Ant illustration"></div>
    <div class="abs bug" style="left:34px;top:692px;width:66px;height:66px" role="img" aria-label="Mosquito illustration"></div>
    <div class="abs bug" style="left:712px;top:780px;width:52px;height:64px" role="img" aria-label="Ant illustration"></div>

    <svg width="0" height="0" style="position:absolute">
      <symbol id="tick" viewBox="0 0 16 12"><path d="M1 6 L6 11 L15 1" fill="none" stroke="currentColor" stroke-width="2.5"/></symbol>
    </svg>

    <ul class="abs service-box" style="left:62px">
      <li><svg class="tick" style="color:var(--brand-red)"><use href="#tick"/></svg>Ants</li>
      <li class="accent"><svg class="tick" style="color:var(--ink)"><use href="#tick"/></svg>Bed Bugs</li>
      <li><svg class="tick" style="color:var(--brand-red)"><use href="#tick"/></svg>Spiders</li>
    </ul>
    <ul class="abs service-box" style="left:275px">
      <li><svg class="tick" style="color:var(--brand-red)"><use href="#tick"/></svg>Cockroaches</li>
      <li class="accent"><svg class="tick" style="color:var(--ink)"><use href="#tick"/></svg>Bees<br>&amp; wasps</li>
      <li><svg class="tick" style="color:var(--brand-red)"><use href="#tick"/></svg>Rodents</li>
    </ul>
    <ul class="abs service-box" style="left:487px">
      <li><svg class="tick" style="color:var(--brand-red)"><use href="#tick"/></svg>Boxelder &amp;<br>elm seed bugs</li>
      <li class="accent"><svg class="tick" style="color:var(--ink)"><use href="#tick"/></svg>Commercial<br>properties</li>
    </ul>

    <div class="abs photo photo-spraying" role="img" aria-label="Technician in orange spraying along a house foundation"></div>
    <div class="abs photo photo-sprayer" role="img" aria-label="Metal sprayer tank and company cap on the lawn"></div>
    <div class="abs photo photo-inspecting" role="img" aria-label="Technician treating the eaves of a house"></div>
  </div>
</div>
</body>
</html>
```